Massage-Creme label for a young pharmacy

We are a young pharmacy which is part of a big union. We developed for a customer a very good massage creme with aloe vera, coconut oil, and many more advantages and as well a massage jelly. All we need is a good and affordable label which is beatiful and helps us to promote our product. As we want to develop further products, it would be very cool to have a corporate label for all upcoming products.

Target Market(s)

professional masseurs and physiotherapists

Industry/Entity Type

Health And Wellness

Font styles to use
Sans Serif
Decorative

Colors

Designer to choose colors to be used in the design.

Requirements
Must have
• Professionally looking design (but I'm sure you are doing so... :-)
Nice to have
• Label can have any shape. What you see is just a bad label with corresponding sizes, so you can imagine how it would look like in the final state.
Should not have
• If possible, the label should not be completely black (although it might look cool) as we are printing it on our own Vostek qr318-ux and black is difficult to print (and very costy).

```html
<!DOCTYPE html>
<html lang="de">
<head>
<meta charset="utf-8">
<title>Massage Crème – Coconut | Aloe Vera</title>
<link rel="stylesheet" href="https://fonts.googleapis.com/css2?family=Bebas+Neue&family=Oswald:wght@200;600;700&family=Open+Sans:wght@400;600;700&display=swap">
<style>
  :root {
    --green-deep: #3fae2a;
    --green-mid: #6cc04a;
    --green-light: #a9d88a;
    --green-pale: #dff0d0;
    --text-dark: #1d1d1b;
    --white: #ffffff;
    --coco-brown: #8a5a34;
  }
  * { margin: 0; padding: 0; box-sizing: border-box; }
  html, body { width: 1200px; height: 979px; overflow: hidden; background: var(--white); }
  .label {
    position: relative; width: 1200px; height: 979px; overflow: hidden;
    font-family: "Open Sans", Arial, sans-serif; color: var(--text-dark);
  }
  .waves { position: absolute; inset: 0; }
  .title {
    position: absolute; left: 160px; top: 112px; margin: 0; font-weight: normal;
    color: var(--white); text-shadow: 0 3px 8px rgba(0,0,0,.18);
  }
  .title-main {
    display: block; font-family: "Bebas Neue", "Arial Narrow", sans-serif;
    font-size: 114px; line-height: 1; letter-spacing: 0;
  }
  .title-sub {
    display: block; font-family: "Oswald", "Arial Narrow", sans-serif; font-weight: 200;
    font-size: 140px; line-height: 1.3; letter-spacing: -4px; margin-top: -30px; margin-left: -4px;
  }
  .variant {
    position: absolute; left: 162px; top: 473px;
    font-family: "Bebas Neue", "Arial Narrow", sans-serif; font-size: 42px; line-height: 1;
    color: var(--green-mid);
  }
  .product-visual {
    position: absolute; left: 172px; top: 528px; width: 300px; height: 305px;
    border-radius: 46% 50% 40% 44%;
    background: linear-gradient(120deg, var(--green-light) 0%, var(--green-mid) 45%, var(--coco-brown) 100%);
    opacity: .85;
  }
  .badge {
    position: absolute; left: 168px; top: 576px; width: 120px; height: 76px;
    border-radius: 50%; background: var(--green-mid); transform: rotate(-14deg);
    border: 2px solid var(--white);
    color: var(--white); font-weight: 700; font-size: 17px; line-height: 1.05;
    display: flex; flex-direction: column; align-items: center; justify-content: center;
    box-shadow: 0 2px 4px rgba(0,0,0,.15);
  }
  .volume { position: absolute; left: 284px; top: 893px; font-size: 17px; color: var(--white); }
  .copy {
    position: absolute; left: 680px; width: 400px; text-align: center; font-size: 13.5px; line-height: 1.42;
  }
  .copy p + p { margin-top: 20px; }
  .copy-intro { top: 142px; }
  .ph-rule { position: absolute; left: 732px; top: 394px; width: 294px; height: 2px; background: var(--green-mid); }
  .ph-rule::after {
    content: ""; position: absolute; left: 143px; top: -3px; width: 8px; height: 8px;
    border-radius: 50%; background: var(--white); border: 2px solid var(--green-mid);
  }
  .copy-quality { top: 440px; font-size: 11px; line-height: 1.5; }
  .free-box {
    position: absolute; left: 713px; top: 492px; width: 332px; height: 65px;
    border: 3px solid var(--green-mid); font-size: 11px; line-height: 1.35;
    text-align: center; padding: 8px 12px; background: var(--white);
  }
  .pharmacy { position: absolute; left: 872px; top: 735px; }
  .pharmacy-brand { font-size: 15px; font-weight: 700; color: var(--green-deep); letter-spacing: 1px; display: flex; align-items: center; gap: 6px; }
  .pharmacy-brand::before { content: ""; width: 9px; height: 9px; border-radius: 50%; background: var(--green-deep); }
  .pharmacy-name { margin-top: 2px; font-size: 10px; font-weight: 600; }
  .pharmacy-contact { margin-top: 22px; font-size: 8.5px; line-height: 1.55; }
  .batch { position: absolute; left: 698px; top: 790px; font-size: 9.5px; line-height: 1.35; }
  .ingredients { position: absolute; left: 698px; top: 836px; width: 380px; font-size: 8px; line-height: 1.5; }
</style>
</head>
<body>
<div class="label">
  <svg class="waves" width="1200" height="979" viewBox="0 0 1200 979" aria-hidden="true">
    <defs>
      <linearGradient id="bandTop" x1="0" y1="0" x2="1" y2="0">
        <stop offset="0" stop-color="#ffffff"/>
        <stop offset=".08" stop-color="#5fb93c"/>
        <stop offset=".6" stop-color="#7cc548"/>
        <stop offset=".9" stop-color="#a9d88a"/>
        <stop offset="1" stop-color="#ffffff"/>
      </linearGradient>
      <linearGradient id="bandLow" x1="0" y1="0" x2="1" y2="0">
        <stop offset="0" stop-color="#ffffff"/>
        <stop offset=".06" stop-color="#5cbb3b"/>
        <stop offset=".7" stop-color="#4db234"/>
        <stop offset=".95" stop-color="#cfe9bd"/>
        <stop offset="1" stop-color="#ffffff"/>
      </linearGradient>
    </defs>
    <rect x="40" y="32" width="1120" height="914" fill="url(#bandTop)"/>
    <path d="M40 330 C 320 460 520 210 760 140 C 900 100 1050 120 1160 90 L1160 946 L40 946 Z" fill="#ffffff"/>
    <path d="M40 360 C 300 520 560 240 800 180 C 960 140 1080 170 1160 150" fill="none" stroke="#cfe9bd" stroke-width="28" opacity=".7"/>
    <path d="M40 560 C 300 700 620 640 900 560 C 1020 530 1110 540 1160 560 L1160 946 L40 946 Z" fill="#cfe9bd" opacity=".7"/>
    <path d="M40 640 C 340 560 620 760 880 690 C 1000 655 1100 600 1160 580 L1160 946 L40 946 Z" fill="url(#bandLow)"/>
    <path d="M300 946 C 520 760 780 760 1160 700 L1160 946 Z" fill="#e8f4de" opacity=".9"/>
    <path d="M520 946 C 700 820 920 800 1160 760 L1160 946 Z" fill="#ffffff"/>
    <rect x="0" y="0" width="40" height="979" fill="#ffffff"/>
    <rect x="1160" y="0" width="40" height="979" fill="#ffffff"/>
    <rect x="0" y="0" width="1200" height="32" fill="#ffffff"/>
    <rect x="0" y="946" width="1200" height="33" fill="#ffffff"/>
  </svg>

  <h1 class="title"><span class="title-main">MASSAGE</span><span class="title-sub">CRÈME</span></h1>
  <div class="variant">COCONUT | ALOE VERA</div>

  <div class="product-visual" role="img" aria-label="Aufgebrochene Kokosnuss vor frischen Aloe-Vera-Blättern"></div>
  <div class="badge"><span>energetisch</span><span>leitend !</span></div>
  <div class="volume">℮ 1000 ml</div>

  <div class="copy copy-intro">
    <p>Hochwertige und sehr hautschonende Emulsion mit<br>hervorragendem Gleitverhalten für die professionelle<br>Massage.</p>
    <p>Hilft durch den hohen Gehalt an Aloe Vera-Gel (50%),<br>die Feuchtigkeit der Haut zu erhalten und schützt<br>durch die Zugabe von Panthenol<br>(= Provitamin B5) und Allantoin vor Hautreizungen.</p>
    <p>Speziell für die (bio-)energetische Massage<br>entwickelt.</p>
    <p>pH-neutral für die Haut (pH-Wert = 5.5)</p>
  </div>
  <div class="ph-rule"></div>

  <div class="copy copy-quality">Bei der Entwicklung unserer Produkte legen wir grössten Wert auf<br>gute Verträglichkeit und hochwertige Rohstoffe.</div>

  <div class="free-box">Dieses Produkt ist frei von Parabenen, Mineralölen<br>(Paraffin/Vaseline), Silikonen, Farbstoffen und Mikroplastik<br>(Acrylate).</div>

  <div class="pharmacy">
    <div class="pharmacy-brand">Medivia</div>
    <div class="pharmacy-name">Apotheke Dr. Lindqvist</div>
    <div class="pharmacy-contact">
      Lindenweg 24, 8700 Seefeld<br>
      Tel. 044 555 12 30, Fax 044 555 12 31<br>
      www.apotheke-lindqvist.ch
    </div>
  </div>

  <div class="batch">Exp: 03/2021<br>Lot: 913015/A</div>

  <div class="ingredients">Zus.: water (aqua), cetearyl isononanoate, ethylhexyl stearate, cocos nucifera (coconut oil), octyldodecanol, glycerol, glyceryl stearate citrate, cetearyl alcohol, phenoxyethanol (and) caprylyl glycol, panthenol, sodium chloride, xanthan gum, disodium hydrogenphosphate, citric acid, aloe barbadensis leaf juice extract, allantoin, parfum</div>
</div>
</body>
</html>
```